Home Page Design

We have a B2B home page design and need a consumer version. The look and feel can look similar but needs to be distinctly different so it in not to get confused. Essentially it should look like the same company with a different model. We will need a PSD w all layers organized and easy to understand. Attached is the logo, B2B comp, and a MS Word doc with a short description. In addition, I have attached a wire frame to be used as a site map. PLEASE DO NOT take that as the creative. I expect to see your creative based on the information provided.

Industry/Entity Type

Consumer

```html
<!DOCTYPE html>
<html lang="en">
<head>
<meta charset="utf-8">
<title>GiveCaddie.com – Home</title>
<link rel="stylesheet" href="https://fonts.googleapis.com/css2?family=Open+Sans:wght@400;600&family=Arimo:wght@400&family=Crimson+Text:wght@400&display=swap">
<style>
:root{
  --green:#3cb54a;
  --blue:#1a6e9a;
  --heading-blue:#1f78a8;
  --ink:#222;
  --nav:#3a3a3a;
  --header-bg:#f5f5f5;
  --hero-band:#dcdcdc;
  --panel-light:#f2f2f2;
  --panel-mid:#e9e9e9;
  --caption:#3a3a3a;
  --field-border:#cfcfcf;
  --field-text:#777;
}
*{margin:0;padding:0;box-sizing:border-box}
html,body{width:1200px;height:994px;overflow:hidden;background:#fff}
body{position:relative;font-family:"Open Sans",sans-serif;color:var(--ink)}
.abs{position:absolute}

.site-header{left:0;top:0;width:1200px;height:86px;background:var(--header-bg);border-bottom:3px solid var(--blue)}
.brand{left:194px;top:12px;display:flex;align-items:center;gap:12px}
.brand-dot{width:62px;height:62px;border-radius:50%;background:var(--blue)}
.brand-name{font-size:23px;color:var(--green);font-weight:400}
.main-nav{top:41px;left:537px;display:flex;gap:27px;font-size:16px;color:var(--nav)}
.main-nav .active{color:var(--green);font-weight:600}
.main-nav span:last-child{margin-left:5px}

.hero-band{left:0;top:89px;width:1200px;height:349px;background:var(--hero-band)}
.hero{left:170px;top:88px;width:882px;height:350px;background:linear-gradient(180deg,#5f8a3a 0%,#6f9a3c 20%,#54708a 35%,#7ea64a 55%,#8fbc4a 100%)}
.hero-caption{left:0;bottom:0;width:100%;height:43px;background:rgba(40,40,40,.88);display:flex;align-items:center;justify-content:space-between;padding:0 18px 0 25px}
.hero-caption h1{font-family:"Crimson Text",serif;font-weight:400;font-size:29px;color:#fff}
.dots{display:flex;gap:7px}
.dots i{width:11px;height:11px;border-radius:50%;background:var(--heading-blue)}
.dots i:first-child{background:var(--green)}

.panel{position:absolute}
.p1{left:168px;top:438px;width:229px;height:256px;background:var(--panel-light)}
.p2{left:397px;top:438px;width:655px;height:256px;background:var(--panel-mid)}
.p3{left:168px;top:694px;width:229px;height:237px;background:var(--panel-mid)}
.p4{left:397px;top:694px;width:655px;height:237px;background:var(--panel-light)}

.search-title{font-family:"Arimo",sans-serif;font-size:14px;color:var(--ink)}
.field{left:176px;width:212px;height:26px;background:#fff;border:1px solid var(--field-border);font-size:13px;color:var(--field-text);padding:4px 12px}
.btn{left:176px;width:79px;height:26px;background:var(--green);color:#fff;font-size:13px;font-weight:600;letter-spacing:.5px;text-align:center;line-height:26px}

.section-title{font-family:"Arimo",sans-serif;font-size:18px;color:var(--heading-blue)}

.card{width:154px;height:172px;border:1px solid #bdbdbd;background:#f4f4f4;padding:4px}
.card-image{width:100%;height:100%;position:relative}
.card-label{position:absolute;left:0;bottom:0;width:100%;height:30px;background:rgba(55,55,55,.9);color:#fff;font-family:"Arimo",sans-serif;font-size:13px;line-height:13px;text-align:center;padding-top:2px}

.site-footer{left:0;top:958px;width:1200px;height:36px;background:var(--blue);color:#fff;font-family:"Arimo",sans-serif;font-size:11px;text-align:center;line-height:36px}
</style>
</head>
<body>
<header class="site-header abs">
  <div class="brand abs"><div class="brand-dot"></div><span class="brand-name">GiveCaddie.com</span></div>
  <nav class="main-nav abs"><span class="active">Post Your Event</span><span>Add Auction Items</span><span>About Us</span><span>Contact Us</span></nav>
</header>

<div class="hero-band abs"></div>
<section class="hero abs" role="img" aria-label="Aerial view of a palm-lined golf course with a lake and sand bunkers">
  <div class="hero-caption abs">
    <h1>Palm Vista Golf Course</h1>
    <div class="dots"><i></i><i></i><i></i><i></i></div>
  </div>
</section>

<div class="panel p1"></div><div class="panel p2"></div><div class="panel p3"></div><div class="panel p4"></div>

<div class="search-title abs" style="left:183px;top:472px">Search for An Auction Item</div>
<div class="field abs" style="top:505px">Auction Type</div>
<div class="field abs" style="top:544px">Auction Date</div>
<div class="field abs" style="top:584px">Charity</div>
<div class="btn abs" style="top:624px">SEARCH</div>

<div class="search-title abs" style="left:176px;top:716px">Search for Golf Events</div>
<div class="field abs" style="top:745px">Event Type</div>
<div class="field abs" style="top:781px">Event Date</div>
<div class="field abs" style="top:818px">Event Location</div>
<div class="field abs" style="top:854px">Event Name</div>
<div class="btn abs" style="top:889px">SEARCH</div>

<h2 class="section-title abs" style="left:408px;top:467px;font-weight:400">Featured Auction Items</h2>
<div class="card abs" style="left:407px;top:504px"><div class="card-image" role="img" aria-label="Candlelit restaurant table with wine glasses" style="background:linear-gradient(160deg,#6b3a1c,#2a1608 60%,#c07a3a)"><div class="card-label">Dinner With<br>Marcus Hale</div></div></div>
<div class="card abs" style="left:567px;top:504px"><div class="card-image" role="img" aria-label="Three bottles of wine on black" style="background:linear-gradient(180deg,#0c0c0c,#222 60%,#3a3a2a)"><div class="card-label">Case of<br>Ridgeline Wine</div></div></div>
<div class="card abs" style="left:728px;top:504px"><div class="card-image" role="img" aria-label="Racing bicycle on warm background" style="background:radial-gradient(circle at 50% 40%,#c98a2a,#5a3410 55%,#1a1208)"><div class="card-label">Velora<br>Bicycle</div></div></div>
<div class="card abs" style="left:889px;top:504px"><div class="card-image" role="img" aria-label="Illuminated tower in a city at night" style="background:linear-gradient(180deg,#0d1a2a,#1c2a3a 50%,#6a5a2a 80%,#2a4a6a)"><div class="card-label">5 Days / 4 Nights<br>In Paris France</div></div></div>

<h2 class="section-title abs" style="left:409px;top:711px;font-weight:400">Featured Golf Events</h2>
<div class="card abs" style="left:407px;top:747px"><div class="card-image" role="img" aria-label="Golf green framed by trees" style="background:linear-gradient(180deg,#7fb4e0,#3e6a2a 35%,#6fae3a 70%,#8cc84a)"><div class="card-label">November 12<br>Riverbend Country Club</div></div></div>
<div class="card abs" style="left:567px;top:747px"><div class="card-image" role="img" aria-label="Aerial view of a seaside golf course" style="background:linear-gradient(180deg,#2a6a9a,#4a8a4a 25%,#6aa84a)"><div class="card-label">November 16<br>Harbor Dunes</div></div></div>
<div class="card abs" style="left:728px;top:747px"><div class="card-image" role="img" aria-label="Island green surrounded by water" style="background:linear-gradient(180deg,#cfe2ef,#3a6a2a 30%,#2a5a8a 60%,#1e4a7a)"><div class="card-label">November 18<br>Sawmill Links</div></div></div>
<div class="card abs" style="left:889px;top:747px"><div class="card-image" role="img" aria-label="Golfers on a fairway lined with trees" style="background:linear-gradient(180deg,#b8c8c8,#2e4a22 30%,#6a9a34 60%,#7eae3a)"><div class="card-label">November 19<br>Palm Vista</div></div></div>

<footer class="site-footer abs">Copyright © 2014&nbsp; GiveCaddie&nbsp; All Rights Reserved.</footer>
</body>
</html>
```